Migration Lawyers

Company: Dunstan & Co Lawyers & Migration Agents

Name: Graham Dunstan BEc, LLB
Address: Level 18, 72 Hollis Street
Sydney, NSW, Australia 2000

Ph: +61 2 9384 5207
M: 0428316540
E: graham@permitpath-example.org.au
W: www.permitpath-example.org.au

Target Market(s)

Migration Clients

Industry/Entity Type

It Company

Font styles to use
Script

Requirements
Must have
• Logo
Should not have
• Please scale the format to the printing size attached

```html
<!DOCTYPE html>
<html lang="en">
<head>
<meta charset="utf-8">
<title>Dunstan &amp; Co – Business Card</title>
<link rel="stylesheet" href="https://fonts.googleapis.com/css2?family=Tinos:wght@400;700&family=Open+Sans:wght@400&display=swap">
<style>
  :root {
    --backdrop: #e8e4dd;
    --paper: #ffffff;
    --ink: #111111;
    --accent-red: #e0231b;
    --soft-grey: #d9d9d9;
    --card-shadow: rgba(0, 0, 0, 0.18);
  }
  * { box-sizing: border-box; margin: 0; padding: 0; }
  html, body {
    width: 1200px;
    height: 1135px;
    overflow: hidden;
    background: var(--backdrop);
  }
  .canvas { position: relative; width: 1200px; height: 1135px; }
  .card {
    position: absolute;
    background: var(--paper);
    box-shadow: 0 2px 6px var(--card-shadow);
    overflow: hidden;
  }
  .card--front { left: 27px; top: 45px; width: 884px; height: 504px; }
  .card--back  { left: 285px; top: 601px; width: 881px; height: 505px; }

  .brand {
    position: absolute;
    display: flex;
    align-items: center;
    gap: 12px;
    font-family: "Tinos", "Times New Roman", serif;
    font-weight: 700;
    color: var(--ink);
  }
  .brand__mark {
    flex: none;
    border-radius: 50%;
    border: 2px solid var(--soft-grey);
    background: var(--paper);
  }
  .brand__name { line-height: 1.1; }
  .brand__title { display: block; font-size: 44px; }
  .brand__tagline { display: block; font-size: 18px; }

  .card--front .brand { left: 108px; top: 50px; }
  .card--front .brand__mark { width: 132px; height: 120px; }

  .card--back .brand { left: 160px; top: 128px; }
  .card--back .brand__mark { width: 200px; height: 165px; }
  .card--back .brand__title { font-size: 50px; }
  .card--back .brand__tagline { font-size: 20px; }

  .holder {
    position: absolute;
    left: 110px;
    top: 232px;
    font-family: "Tinos", "Times New Roman", serif;
    font-size: 26px;
    color: var(--ink);
  }
  .holder__name { font-weight: 700; }
  .holder__quals { font-weight: 400; font-size: 22px; color: #333; }

  .contact-list {
    position: absolute;
    left: 110px;
    top: 287px;
    list-style: none;
    font-family: "Open Sans", Arial, sans-serif;
    font-size: 18px;
    color: var(--ink);
  }
  .contact-list li {
    display: flex;
    align-items: center;
    gap: 10px;
    height: 37px;
  }
  .contact-list svg { width: 16px; height: 16px; flex: none; }

  .corner-band { position: absolute; left: 0; top: 0; width: 884px; height: 504px; }

  .address {
    position: absolute;
    right: 22px;
    top: 418px;
    text-align: right;
    font-family: "Open Sans", Arial, sans-serif;
    font-size: 17px;
    line-height: 32px;
    color: var(--paper);
  }

  .back-url {
    position: absolute;
    left: 0;
    width: 100%;
    top: 382px;
    text-align: center;
    font-family: "Open Sans", Arial, sans-serif;
    font-size: 25px;
    letter-spacing: 2.5px;
    color: var(--ink);
  }
</style>
</head>
<body>
<main class="canvas">

  <section class="card card--front" aria-label="Business card front">
    <svg class="corner-band" viewBox="0 0 884 504" aria-hidden="true">
      <polygon points="600,404 884,404 884,504 548,504" fill="var(--ink)"/>
      <polygon points="610,390 884,390 884,396 606,396" fill="var(--accent-red)"/>
      <rect x="0" y="496" width="548" height="8" fill="var(--accent-red)"/>
    </svg>

    <div class="brand">
      <span class="brand__mark"></span>
      <span class="brand__name">
        <span class="brand__title">Dunstan &amp; Co</span>
        <span class="brand__tagline">Lawyers &amp; Migration Agents</span>
      </span>
    </div>

    <p class="holder"><span class="holder__name">Graham Dunstan,</span> <span class="holder__quals">BEc, LLB</span></p>

    <ul class="contact-list">
      <li>
        <svg viewBox="0 0 16 16" aria-hidden="true"><circle cx="8" cy="8" r="8" fill="var(--accent-red)"/><path d="M5 4.5c0 4 2.5 6.5 6.5 6.5l.5-1.6-1.8-.8-.8.9c-1.2-.5-2.2-1.5-2.7-2.7l.9-.8-.8-1.8Z" fill="#fff"/></svg>
        +61 2 9384 5207
      </li>
      <li>
        <svg viewBox="0 0 16 16" aria-hidden="true"><rect x="3.5" y="1" width="9" height="14" rx="2" fill="var(--accent-red)"/><rect x="5.5" y="3.5" width="5" height="5" fill="#fff"/></svg>
        0428316540
      </li>
      <li>
        <svg viewBox="0 0 16 16" aria-hidden="true"><rect x="1" y="3" width="14" height="10" rx="2" fill="var(--accent-red)"/><path d="M2.5 5 8 9l5.5-4" stroke="#fff" stroke-width="1.3" fill="none"/></svg>
        graham@permitpath-example.org.au
      </li>
      <li>
        <svg viewBox="0 0 16 16" aria-hidden="true"><circle cx="8" cy="8" r="8" fill="var(--accent-red)"/><path d="M2 8h12M8 2v12" stroke="#fff" stroke-width="1.2" fill="none"/></svg>
        www.permitpath-example.org.au
      </li>
    </ul>

    <p class="address">Level 18, 72 Hollis Street<br>Australia, Sydney, NSW, 2000</p>
  </section>

  <section class="card card--back" aria-label="Business card back">
    <div class="brand">
      <span class="brand__mark"></span>
      <span class="brand__name">
        <span class="brand__title">Dunstan &amp; Co</span>
        <span class="brand__tagline">Lawyers &amp; Migration Agents</span>
      </span>
    </div>
    <p class="back-url">www.permitpath-example.org.au</p>
  </section>

</main>
</body>
</html>
```